Hair dresser flyer for Air conditioning heat pumps A5

We require a flyer that is selling the benifits of air conditioning heat pumps which cools in summer and efficently heats in winter. Colour should be white background. Red and blue from logo to represent the Air conditioning Heat pump does heating and cooling and energy effient.

Target Market(s)

Hairdressor, Salons , barbers ,

Colors
0054AA
0677BA
7BADD7
CADEEF
E8F1F8
EB3D1F
EC4F4E
F09395
F8D3D4
FCEDEE

Requirements
Must have
• Cost from

```html
<!DOCTYPE html>
<html lang="en">
<head>
<meta charset="utf-8">
<title>Calderwood – Air Conditioning Heat Pumps Flyer</title>
<link href="https://fonts.googleapis.com/css2?family=Roboto:ital,wght@0,400;0,500;0,700;0,900;1,400&display=swap" rel="stylesheet">
<style>
  :root{
    --blue-dark:#0054AA;
    --blue:#0677BA;
    --blue-bright:#2a9ad6;
    --blue-light:#7BADD7;
    --red:#EB3D1F;
    --orange:#E8522A;
    --red-deep:#B01E10;
    --ink:#1a1a1a;
    --paper:#ffffff;
    --backdrop:#8e9193;
  }
  *{box-sizing:border-box;margin:0;padding:0}
  html,body{width:960px;height:1200px;overflow:hidden}
  body{background:var(--backdrop);font-family:"Roboto",sans-serif;position:relative}

  .page{position:absolute;top:303px;width:420px;height:594px;background:var(--paper);overflow:hidden;box-shadow:0 10px 30px rgba(0,0,0,.25)}
  .page--front{left:510px}
  .page--back{left:30px}
  .shapes{position:absolute;inset:0;width:100%;height:100%}
  .abs{position:absolute}

  /* front */
  .brand{left:26px;top:22px;display:flex;align-items:center;gap:8px}
  .brand__mark{width:10px;height:10px;background:var(--red)}
  .brand__name{font-weight:900;font-size:32px;color:var(--ink);letter-spacing:-.5px;line-height:1}
  .brand__tag{left:44px;top:58px;font-size:10px;font-style:italic;color:var(--ink)}
  .headline{font-weight:900;font-size:12.5px;line-height:1.3;text-transform:uppercase;color:var(--ink)}
  .headline--lead{left:24px;top:92px;width:210px}
  .headline--offer{left:24px;top:158px;width:390px}
  .benefits{left:22px;top:250px;list-style:none;color:#fff;font-size:14.5px;font-weight:500}
  .benefits li{display:flex;align-items:center;gap:6px;line-height:19px}
  .benefits svg{width:11px;height:11px;flex:none}
  .about{left:24px;top:462px;width:376px;color:#fff;font-size:7.6px;line-height:1.35}
  .about p+p{margin-top:7px}

  /* back */
  .intro{left:22px;top:20px;width:380px;font-size:9px;line-height:1.35;color:var(--ink)}
  .example{left:22px;top:342px;width:260px;font-size:9.5px;line-height:1.3;color:var(--ink)}
  .contact{left:24px;top:506px;color:#fff;font-size:11.5px;line-height:1.35}
  .contact__row{display:flex;align-items:center;gap:6px;margin-top:2px}
  .contact__row svg{width:10px;height:10px;flex:none}
</style>
</head>
<body>

<!-- Front -->
<section class="page page--front">
  <svg class="shapes" viewBox="0 0 420 594" aria-hidden="false">
    <defs>
      <linearGradient id="salonTones" x1="0" y1="0" x2="1" y2="1">
        <stop offset="0" stop-color="#d9c9c4"/><stop offset=".5" stop-color="#e8b7ad"/><stop offset="1" stop-color="#a8a6a3"/>
      </linearGradient>
      <linearGradient id="unitTones" x1="0" y1="0" x2="1" y2="1">
        <stop offset="0" stop-color="#e4e2e0"/><stop offset=".55" stop-color="#3a3a3c"/><stop offset="1" stop-color="#1c1c1e"/>
      </linearGradient>
      <linearGradient id="blueBlock" x1="0" y1="0" x2="1" y2="1">
        <stop offset="0" stop-color="#2a9ad6"/><stop offset="1" stop-color="#1c86c8"/>
      </linearGradient>
    </defs>
    <polygon points="300,82 420,70 420,200 218,200" fill="url(#salonTones)" role="img" aria-label="Photo of a salon interior with a wall-mounted air conditioning unit"/>
    <polygon points="296,82 310,81 232,200 218,200" fill="var(--blue-bright)"/>
    <polygon points="232,170 250,170 232,200 212,200" fill="var(--red)"/>
    <polygon points="0,238 372,238 262,420 0,420" fill="var(--orange)"/>
    <polygon points="392,252 420,252 420,430 280,430" fill="url(#unitTones)" role="img" aria-label="Photo of a black wall-mounted heat pump unit"/>
    <polygon points="0,432 40,432 20,452 0,452" fill="var(--orange)"/>
    <polygon points="0,448 420,438 420,594 0,594" fill="url(#blueBlock)"/>
  </svg>

  <div class="brand abs">
    <span class="brand__mark"></span>
    <span class="brand__name">Calderwood</span>
  </div>
  <p class="brand__tag abs">Temperature solutions for business.</p>

  <p class="headline headline--lead abs">Save £££ on your shops heating costs and stay cool in the summer</p>
  <p class="headline headline--offer abs">Energy- efficient<br>air conditioning heat pumps installed<br>from £1750 + VAT</p>

  <ul class="benefits abs">
    <li><svg viewBox="0 0 12 12"><path d="M1 6.5 4.5 10 11 2" fill="none" stroke="#fff" stroke-width="2"/></svg>Cools in Summer</li>
    <li><svg viewBox="0 0 12 12"><path d="M1 6.5 4.5 10 11 2" fill="none" stroke="#fff" stroke-width="2"/></svg>Efficient Heats in Winter</li>
    <li><svg viewBox="0 0 12 12"><path d="M1 6.5 4.5 10 11 2" fill="none" stroke="#fff" stroke-width="2"/></svg>More Productive staff</li>
    <li><svg viewBox="0 0 12 12"><path d="M1 6.5 4.5 10 11 2" fill="none" stroke="#fff" stroke-width="2"/></svg>Increased Sales</li>
    <li><svg viewBox="0 0 12 12"><path d="M1 6.5 4.5 10 11 2" fill="none" stroke="#fff" stroke-width="2"/></svg>Reduce cancellation in Summer</li>
    <li><svg viewBox="0 0 12 12"><path d="M1 6.5 4.5 10 11 2" fill="none" stroke="#fff" stroke-width="2"/></svg>Filters and cleans the air</li>
    <li><svg viewBox="0 0 12 12"><path d="M1 6.5 4.5 10 11 2" fill="none" stroke="#fff" stroke-width="2"/></svg>Reduced allergens &amp; Bugs</li>
    <li><svg viewBox="0 0 12 12"><path d="M1 6.5 4.5 10 11 2" fill="none" stroke="#fff" stroke-width="2"/></svg>Reduce Humidity</li>
  </ul>

  <div class="about abs">
    <p>Air Conditioning Heat Pumps creates the ideal environment all year round for staff to be at there most productive and for consumers to spend more time and, accordingly, more money.</p>
    <p>Modern Air Conditioning Heat pumps are one of the most energy efficient forms of heating available and ideal for those looking for a simple cost effective way to heat and cool the space. They are easy to install and operate and can quickly provide with the comfort you need.</p>
    <p>Reduce cancelations and absences in the warm summer months with Cooling mode. With the warms temperatures inside hairdressers and salons and clients not wanting to sit in somewhere with extreme heat.</p>
  </div>
</section>

<!-- Back -->
<section class="page page--back">
  <svg class="shapes" viewBox="0 0 420 594">
    <defs>
      <linearGradient id="studioTones" x1="0" y1="0" x2="1" y2="1">
        <stop offset="0" stop-color="#e9e4df"/><stop offset=".5" stop-color="#b89a86"/><stop offset="1" stop-color="#6e5a4e"/>
      </linearGradient>
      <linearGradient id="vanTones" x1="0" y1="0" x2="1" y2="1">
        <stop offset="0" stop-color="#efe7e3"/><stop offset="1" stop-color="#c9b9b2"/>
      </linearGradient>
      <linearGradient id="wallTones" x1="0" y1="0" x2="1" y2="1">
        <stop offset="0" stop-color="#5f7a45"/><stop offset="1" stop-color="#e3c4be"/>
      </linearGradient>
      <linearGradient id="contactBand" x1="0" y1="0" x2="1" y2="0">
        <stop offset="0" stop-color="var(--orange)"/><stop offset=".6" stop-color="var(--red)"/><stop offset="1" stop-color="var(--red-deep)"/>
      </linearGradient>
    </defs>
    <polygon points="0,96 420,88 420,300 0,332" fill="url(#studioTones)" role="img" aria-label="Photo of a salon with styling stations and a ceiling cassette air conditioner"/>
    <polygon points="0,420 200,410 190,500 0,500" fill="url(#vanTones)" role="img" aria-label="Photo of a salon window with a service van parked outside"/>
    <polygon points="222,340 420,330 420,500 210,500" fill="url(#wallTones)" role="img" aria-label="Photo of a salon entrance with a green plant wall"/>
    <polygon points="0,492 420,486 420,594 0,594" fill="url(#contactBand)"/>
  </svg>

  <p class="intro abs">Reduce heating energy cost by up to 75% vs electric heating. Air conditioning heat pumps is a more efficient heating solution in comparison to a standard electric heaters which are still used in many businesses. This is because air conditioning produces more heat for the amount of electricity it takes to power the unit.</p>

  <p class="example abs">Here's an example to illustrate how an air conditioning heat pump compares over an electric heaters<br>2 x 2kw Electric fan heaters<br>4kw Electricity input = 4kw heat Output<br>4kw Air Conditioning heat pump<br>1kw Electricty input = 4kw Heat output</p>

  <div class="contact abs">
    <p>If you are interested in having air conditioning installed<br>in your business, then give us a call on</p>
    <p class="contact__row"><svg viewBox="0 0 12 12"><path d="M3 1h2l1 3-1.5 1a6 6 0 0 0 2.5 2.5L8 6l3 1v2a1.5 1.5 0 0 1-1.5 1.5A8.5 8.5 0 0 1 1.5 2.5 1.5 1.5 0 0 1 3 1z" fill="#fff"/></svg>01234 567890</p>
    <p class="contact__row"><svg viewBox="0 0 12 12"><circle cx="6" cy="6" r="5" fill="none" stroke="#fff" stroke-width="1.2"/><path d="M1 6h10M6 1c-2.5 3-2.5 7 0 10M6 1c2.5 3 2.5 7 0 10" fill="none" stroke="#fff" stroke-width="1"/></svg>www.calderwood.cool</p>
  </div>
</section>

</body>
</html>
```